Olive Oil 500ml bottle Lable

Dear Designer,

We would like you to design a high quality high class Olive Oil label for a 500ml Dark Round Bottle. (I have attached a image of the bottle)

The olive oil is a premium Australian Product so the design must reflect that. my requirements are all as follows

I have attached the master artwork files for a previous design and require you to submit a totally new design within the exact same size proportions. 190mmx66mm

The brand will be Marvelle Ridge Olive Oil Gold and i have attached our Wine label so that you can use our brand logo.

I wish for the label to be color themed Gold foil printing on perhaps a red background i wish the label to be of abstract aboriginal art consisting of a olive tree and a Kangaroo and emu facing each other on either side of the tree as on the "Australian code of Arms". I wish the tree and the Kangaroo and Emu the be in gold abstract. and possibly a red background. i have attached some images to inspire design of olive trees, kangaroos and emus in the aboriginial abstract art i wish to reflect. i what the dots making up the picture all the be in gold.

The back label can be almost exactly the same except for the change of brand name and colour theme to much the front. The detail at bottom which will be changed to the text bellow.

Produced By: Blue Finch Trading
Address: Shop 4, 218 Upper Wattlefield Road Campbelltown SA 5074
Website: www.bluefinchtrading.example
INGREDIENTS: 100% AUSTRALIAN EXTRA VIRGIN OLIVE OIL

please also leave the space for the bar code on the back label as is on the sample attached

Thank you and i look forward to the designs

Target Market(s)

Chinese Market
Expensive Gift

Requirements
Must have
• The same nutrition chart and descriptive text as on previous label (attached)
• Space for Barcode on rear lable
• The same product information as on sample (attached) eg Australian First Cold Pressed Olive Oil, 500ml 16.9 fl oz, 100% product of Australia, Extra Virgin Olive Oil
Nice to have
• Cheap real life images/Photos

```html
<!DOCTYPE html>
<html lang="en">
<head>
<meta charset="utf-8">
<title>Serafina – Marvelle Ridge Olive Oil Label</title>
<link href="https://fonts.googleapis.com/css2?family=Cinzel:wght@400;700&family=Josefin+Sans:wght@300&family=Open+Sans:wght@400&display=swap" rel="stylesheet">
<style>
  :root {
    --page: #ffffff;
    --maroon: #7a0711;
    --maroon-deep: #4e0309;
    --gold-dark: #b08a34;
    --gold-light: #f7ecaa;
    --cream: #fbf4de;
    --ink: #2a1a0a;
    --white: #ffffff;
  }
  * { margin: 0; padding: 0; box-sizing: border-box; }
  html, body {
    width: 1200px; height: 1000px; overflow: hidden;
    background: var(--page);
  }
  .canvas { position: relative; width: 1200px; height: 1000px; }

  .label {
    position: absolute; left: 466px; top: 114px;
    width: 268px; height: 772px;
    background: var(--maroon);
    border-radius: 12px;
    border: 1px solid #5a2a40;
    overflow: hidden;
  }
  .tree-mark {
    position: absolute; left: 92px; top: 22px; width: 84px; height: 140px;
    background: radial-gradient(ellipse at 50% 45%, rgba(217,194,102,0.85) 0%, rgba(158,165,58,0.6) 40%, rgba(122,7,17,0) 70%);
    border-radius: 50%;
  }
  .origin {
    position: absolute; left: 0; right: 0; top: 168px;
    text-align: center; color: var(--cream);
    font-family: "Cinzel", serif; font-size: 15px; line-height: 19px; letter-spacing: 0.3px;
  }
  .frame, .olive-art { position: absolute; left: 0; top: 0; width: 268px; height: 772px; }
  .product-name {
    position: absolute; left: 0; right: 0; top: 350px;
    text-align: center; color: var(--white);
    font-family: "Cinzel", serif; font-weight: 700; font-size: 42px; letter-spacing: 0.5px;
  }
  .estate {
    position: absolute; left: 0; right: 0; top: 420px;
    text-align: center; color: var(--cream);
    font-family: "Cinzel", serif; font-size: 27px; line-height: 36px;
  }
  .oil-type {
    position: absolute; left: 0; right: 0; top: 522px;
    text-align: center; color: var(--white);
    font-family: "Josefin Sans", sans-serif; font-weight: 300; font-size: 33px; letter-spacing: 1px;
  }
  .gold-band {
    position: absolute; left: 0; right: 0; top: 592px; height: 72px;
    background: linear-gradient(90deg, var(--gold-dark), var(--gold-light) 40%, #e9d37c 70%, var(--gold-dark));
    text-align: center; color: var(--ink);
    font-family: "Cinzel", serif; font-size: 14px; line-height: 17px; padding-top: 20px;
  }
  .gold-stripe {
    position: absolute; left: 0; right: 0; top: 680px; height: 10px;
    background: linear-gradient(90deg, var(--gold-dark), var(--gold-light) 45%, var(--gold-dark));
  }
  .volume {
    position: absolute; left: 0; right: 0; top: 716px;
    text-align: center; color: var(--white);
    font-family: "Open Sans", sans-serif; font-size: 14px;
  }
</style>
</head>
<body>
<div class="canvas">
  <div class="label">
    <div class="tree-mark" role="img" aria-label="Golden olive tree emblem"></div>
    <div class="origin">Australian<br>First Cold Pressed</div>

    <svg class="frame" viewBox="0 0 268 772" aria-hidden="true">
      <defs>
        <linearGradient id="frameGold" x1="0" y1="0" x2="1" y2="1">
          <stop offset="0" stop-color="#d6e08a"/>
          <stop offset="0.5" stop-color="#7f9a2c"/>
          <stop offset="1" stop-color="#c9d470"/>
        </linearGradient>
        <linearGradient id="panelOlive" x1="0" y1="0" x2="0" y2="1">
          <stop offset="0" stop-color="#8c9a3c"/>
          <stop offset="1" stop-color="#5f6e22"/>
        </linearGradient>
      </defs>
      <path fill="url(#frameGold)" d="M30 330 C30 250 60 216 134 216 C208 216 238 250 238 330 C238 380 225 400 225 440 C225 480 256 500 256 540 L256 560 Q256 586 230 586 L38 586 Q12 586 12 560 L12 540 C12 500 43 480 43 440 C43 400 30 380 30 330 Z"/>
      <path fill="url(#panelOlive)" d="M40 330 C40 258 66 226 134 226 C202 226 228 258 228 330 C228 380 215 400 215 440 C215 482 246 502 246 540 L246 556 Q246 576 226 576 L42 576 Q22 576 22 556 L22 540 C22 502 53 482 53 440 C53 400 40 380 40 330 Z"/>
      <rect x="26" y="506" width="216" height="66" rx="8" fill="var(--maroon-deep)"/>
      <line x1="30" y1="506" x2="238" y2="506" stroke="#c9d470" stroke-width="2"/>
      <line x1="40" y1="574" x2="228" y2="574" stroke="#f2e6a0" stroke-width="3"/>
    </svg>

    <svg class="olive-art" viewBox="0 0 268 772" role="img" aria-label="Black olives with green leaves">
      <defs>
        <clipPath id="panelTop">
          <path d="M40 330 C40 258 66 226 134 226 C202 226 228 258 228 330 C228 360 224 372 222 380 L46 380 C44 372 40 360 40 330 Z"/>
        </clipPath>
        <radialGradient id="oliveTones" cx="0.55" cy="0.5" r="0.6">
          <stop offset="0" stop-color="#1c1f14"/>
          <stop offset="0.55" stop-color="#3f5318"/>
          <stop offset="1" stop-color="#8c9a3c" stop-opacity="0"/>
        </radialGradient>
      </defs>
      <rect x="30" y="220" width="210" height="165" fill="url(#oliveTones)" clip-path="url(#panelTop)"/>
    </svg>

    <div class="product-name">Serafina</div>
    <div class="estate">Marvelle<br>Ridge</div>
    <div class="oil-type">OLIVE OIL</div>

    <div class="gold-band">100%<br>Product of Australia</div>
    <div class="gold-stripe"></div>
    <div class="volume">500 ml 16.9 fl oz</div>
  </div>
</div>
</body>
</html>
```